tiling company needs letterhead urgent

We need a logo to represent our company on an electronic letterhead. We are a tiling firm called Corwell Tiling Ltd and undertake all aspects of tiling work. The final design of the logo should incorporate the type of work we do and should be modern. We do not want any designs which may be considered 'novelty' or 'cartoonish.' No characters please, we require something sleek and contemporary . Please ensure the company name is central to your design ,Corwell Tiling Ltd

Industry/Entity Type

Electronic

Requirements
Must have
• text on letterhead to included

Registered address 41 Birch lane Failsworth Manchester M359QT
Company number 5267093
VAT no 412957386
Mobile no 07831659047
Office no 0161 574 8192
Web :www.floorvane.co.uk
Email : gareth@floorvane.co.uk
Nice to have
• a tile theme

```html
<!DOCTYPE html>
<html lang="en">
<head>
<meta charset="utf-8">
<title>Corwell Tiling Ltd – Letterhead</title>
<link href="https://fonts.googleapis.com/css2?family=Open+Sans:wght@400&family=Exo+2:wght@600;700&display=swap" rel="stylesheet">
<style>
  :root {
    --lime: #a6cf4e;
    --leaf: #5fb946;
    --bright: #5dbf3f;
    --pine: #1f8a3a;
    --ink: #222222;
    --paper: #ffffff;
  }
  html, body {
    margin: 0;
    padding: 0;
    width: 848px;
    height: 1200px;
    overflow: hidden;
    background: var(--paper);
  }
  .sheet {
    position: relative;
    width: 800px;
    height: 1132px;
    transform: scale(1.06);
    transform-origin: top left;
    background: var(--paper);
    overflow: hidden;
  }

  .header-field {
    position: absolute;
    left: 0; top: 0;
    width: 495px; height: 190px;
    background: linear-gradient(90deg, var(--bright) 0%, var(--leaf) 45%, var(--lime) 100%);
  }
  .footer-field {
    position: absolute;
    left: 305px; top: 878px;
    width: 495px; height: 254px;
    background: linear-gradient(135deg, var(--lime) 0%, var(--leaf) 45%, var(--pine) 100%);
  }

  .brand {
    position: absolute;
    left: 38px; top: 38px;
    width: 152px; height: 152px;
    display: flex;
    flex-direction: column;
    align-items: center;
    justify-content: center;
    gap: 14px;
  }
  .brand-mark {
    width: 34px; height: 34px;
    background: var(--paper);
  }
  .brand-name {
    font-family: "Exo 2", sans-serif;
    font-weight: 700;
    color: var(--paper);
    font-size: 19px;
    line-height: 1.15;
    text-align: center;
    margin: 0;
  }

  .letter {
    position: absolute;
    left: 60px;
    top: 228px;
    width: 680px;
    font-family: "Open Sans", sans-serif;
    font-size: 15.8px;
    letter-spacing: 0.3px;
    line-height: 19.6px;
    color: var(--ink);
  }
  .letter p { margin: 0 0 19.6px; }
  .salutation { margin-left: 82px !important; }
  .sign-off { margin-top: 8px !important; margin-bottom: 36px !important; }

  .contact {
    position: absolute;
    right: 28px;
    top: 912px;
    margin: 0;
    font-family: "Exo 2", sans-serif;
    font-weight: 600;
    font-size: 14.2px;
    line-height: 20.2px;
    color: var(--paper);
    text-align: right;
    font-style: normal;
  }
</style>
</head>
<body>
<div class="sheet">
  <div class="header-field" role="img" aria-label="Green tile-themed header band"></div>

  <div class="brand">
    <div class="brand-mark"></div>
    <p class="brand-name">Corwell<br>Tiling Ltd</p>
  </div>

  <main class="letter">
    <p class="salutation">Dear Ms. Hart:</p>
    <p style="margin-top:36px">I am writing to ask if you would pass along a request to Lena Marlowe.</p>
    <p>Two years ago, I had hit "rock bottom"-- I was agoraphobic, and had been unable to leave my house for more than a year.&nbsp; Prior to that time, I was a stage actress with aspirations to move to L.A. and start a film career.&nbsp; Panic disorder erased that dream for me, and I had given up on life.</p>
    <p>About this time, I saw the NVT documentary "Panic," and was floored when I heard Ms. Marlowe discussing the very same experiences I'd been having.&nbsp; I am so thankful for her honesty and grateful for the hope she gave me.&nbsp; After watching the show, I didn't feel so crazy, after all.&nbsp; It was so inspiring for me to find out that someone who'd been as low as I was had battled this disorder and fought so hard to keep her dreams alive.</p>
    <p>The worst parts of this disorder were the loneliness and hopelessness, and it was easy to feel like no one else in the world had ever gone through what I had and managed to live a successful life.&nbsp; I promised myself that if I ever overcame agoraphobia, I would remember to pass on that hope to others.&nbsp; That day has finally come, and I'm keeping that promise.</p>
    <p>I have compiled an anthology of success stories from people who have overcome all sorts of anxiety disorders.&nbsp; There are 33 stories in total, from people all over the world, and Dr. Alan Reeve (author of Walking Through Fear) has provided commentaries about each of the stories.&nbsp; The book, Beyond Panic and Anxiety Disorders, is under contract and will be published in paperback and hardcover by Ashgrove Press in fall, 2002.</p>
    <p>Thank you very much for taking the time to read this.&nbsp; Please feel free to contact me anytime by phone or e-mail.&nbsp; I look forward to your response.</p>
    <p class="sign-off">Regards,</p>
    <p>Clara Westing</p>
  </main>

  <div class="footer-field" role="img" aria-label="Green tile-themed footer band"></div>

  <address class="contact">
    41 Birch lane,<br>
    Failsworth<br>
    Manchester, M359QT<br>
    Company number 5267093<br>
    VAT no 412957386<br>
    Mobile 07831659047<br>
    Office 0161 574 8192<br>
    gareth@floorvane.co.uk<br>
    www.floorvane.co.uk
  </address>
</div>
</body>
</html>
```